Want to incorporate elements of all these items to make an amazing sign to welcome people to the community. The sign is 6x4 and needs to incorporate the following items:

Welcome to Corwick Meadows

Come visit the PRD sales center at 745 thistledown road
High Speed Fiber Internet
Land financing starting at $299 (No credit checks)
Let us build your dream home!
555-284-7390
We like the gold and black design no teal or blue that was another agents design. Some combination of the current sign all the stuff listed above and then design elements that tie into the truck wrap.

Target Market(s)

People visiting the neighborhood

Industry/Entity Type

real estate and construction

Font styles to use
Serif

Colors

Designer to choose colors to be used in the design.

Requirements
Must have
• PRD Home Builders Welcomes you to Corwick Meadows, Let us build your dream home, Phone number, Land financing starting at $299 NO credit checks

```html
<!DOCTYPE html>
<html lang="en">
<head>
<meta charset="utf-8">
<title>Welcome to Corwick Meadows</title>
<link rel="stylesheet" href="https://fonts.googleapis.com/css2?family=Andika:wght@400;700&family=Archivo+Black&family=Bungee+Inline&family=Yellowtail&display=swap">
<style>
  :root {
    --ink: #1a1d25;
    --ink-soft: #2b2e35;
    --gold: #dca851;
    --gold-deep: #b07a24;
    --white: #ffffff;
  }
  html, body {
    margin: 0;
    padding: 0;
    width: 1200px;
    height: 800px;
    overflow: hidden;
    background: var(--ink);
  }
  .sign {
    display: block;
    width: 1200px;
    height: 800px;
  }
  .welcome {
    font-family: "Andika", sans-serif;
    font-weight: 700;
    font-size: 84px;
    fill: var(--white);
  }
  .community-name {
    font-family: "Bungee Inline", sans-serif;
    font-size: 118px;
    fill: var(--gold);
  }
  .feature-lead {
    font-family: "Andika", sans-serif;
    font-size: 26px;
    letter-spacing: 1px;
    fill: var(--white);
  }
  .feature-main {
    font-family: "Andika", sans-serif;
    font-size: 44px;
    letter-spacing: 2px;
    fill: var(--white);
  }
  .feature-note {
    font-family: "Andika", sans-serif;
    font-size: 21px;
    letter-spacing: 1px;
    fill: var(--white);
  }
  .tagline {
    font-family: "Yellowtail", cursive;
    font-size: 86px;
    fill: var(--white);
    stroke: var(--gold);
    stroke-width: 9px;
    stroke-linejoin: round;
    paint-order: stroke fill;
  }
  .call-today {
    font-family: "Yellowtail", cursive;
    font-size: 62px;
    fill: var(--gold);
  }
  .phone {
    font-family: "Archivo Black", sans-serif;
    font-size: 82px;
    fill: var(--white);
  }
  .icon { fill: url(#gold-sheen); }
  .icon-line { stroke: var(--gold); stroke-width: 3; stroke-linecap: round; fill: none; }
</style>
</head>
<body>
<svg class="sign" viewBox="0 0 1200 800" xmlns="http://www.w3.org/2000/svg">
  <defs>
    <linearGradient id="backdrop" x1="0" y1="0" x2="0" y2="1">
      <stop offset="0" stop-color="#1a1d25"/>
      <stop offset="0.45" stop-color="#1c1f27"/>
      <stop offset="1" stop-color="#2c2f35"/>
    </linearGradient>
    <linearGradient id="gold-sheen" x1="0" y1="0" x2="1" y2="1">
      <stop offset="0" stop-color="#e3b05a"/>
      <stop offset="1" stop-color="#a8701e"/>
    </linearGradient>
  </defs>

  <rect class="backdrop" width="1200" height="800" fill="url(#backdrop)" role="img" aria-label="Darkened aerial photograph of the neighborhood lots and streets"/>

  <text class="welcome" x="600" y="118" text-anchor="middle">Welcome to</text>
  <text class="community-name" x="64" y="244" textLength="1074" lengthAdjust="spacingAndGlyphs">CORWICK MEADOWS</text>

  <!-- Sales center -->
  <g class="icon-megaphone" transform="translate(66 311)">
    <path class="icon" d="M4 50 q-4 8 0 18 l8 0 0-18z"/>
    <path class="icon" d="M10 46 l40 -6 l52 -30 l0 72 l-52 -20 l-40 0 z"/>
    <ellipse cx="56" cy="44" rx="6" ry="7" fill="var(--ink)"/>
    <circle cx="20" cy="55" r="7" fill="var(--ink)"/>
    <circle cx="20" cy="55" r="4" class="icon"/>
    <path class="icon" d="M22 66 l12 0 l8 22 l-8 2 z"/>
    <path class="icon-line" d="M68 16 l8 -10 M76 28 l12 -6 M80 48 l14 -4 M82 64 l12 0 M80 78 l12 4"/>
  </g>
  <text class="feature-lead" x="208" y="340">Come visit the PRD sales center at</text>
  <text class="feature-main" x="208" y="390">745 THISTLEDOWN ROAD</text>

  <!-- Internet -->
  <g class="icon-signal" transform="translate(66 464)">
    <path class="icon" d="M0 16 q40 -34 80 0 l-10 10 q-30 -24 -60 0z"/>
    <path class="icon" d="M18 34 q22 -18 44 0 l-10 10 q-12 -10 -24 0z"/>
    <path class="icon" d="M70 30 l-30 34 q-6 6 -10 0 q-4 -6 2 -10 z"/>
    <circle cx="35" cy="60" r="3" fill="var(--ink)"/>
  </g>
  <text class="feature-main" x="208" y="500">HIGH SPEED</text>
  <text class="feature-lead" x="208" y="535">Fiber Internet</text>

  <!-- Financing -->
  <g class="icon-post" transform="translate(66 615)">
    <rect class="icon" x="36" y="0" width="10" height="6"/>
    <rect class="icon" x="21" y="6" width="40" height="26"/>
    <rect class="icon" x="36" y="32" width="10" height="22"/>
    <path class="icon" d="M36 54 l10 0 l0 6 l12 0 l14 18 l-62 0 l14 -18 l12 0z"/>
    <rect class="icon" x="0" y="78" width="82" height="5"/>
  </g>
  <text class="feature-lead" x="208" y="633">Land Financing</text>
  <text class="feature-main" x="208" y="680">STARTING AT $299</text>
  <text class="feature-note" x="208" y="707">(no credits checks)</text>

  <!-- Tagline -->
  <g class="tagline-group" transform="rotate(-14 880 470)">
    <text class="tagline" x="884" y="455" text-anchor="middle">Let us build your</text>
    <text class="tagline" x="912" y="530" text-anchor="middle">dream home!</text>
  </g>

  <!-- Call to action -->
  <text class="call-today" x="798" y="676">Call today!</text>
  <text class="phone" x="643" y="750" textLength="512" lengthAdjust="spacingAndGlyphs">555-284-7390</text>
</svg>
</body>
</html>
```